How to find Your Soulmate, Workshop Flyer

Hi Guys, Im after a flyer to promote my workshop on how to find your soulmate, your ideal partner.Love to see what you come up with.
Dom

```html
<!DOCTYPE html>
<html lang="en">
<head>
<meta charset="utf-8">
<title>Soulmate Workshop Flyer</title>
<link href="https://fonts.googleapis.com/css2?family=Montserrat:wght@500;600&family=Open+Sans:wght@400;600&display=swap" rel="stylesheet">
<style>
  :root {
    --paper: #ffffff;
    --ink: #2b2b2b;
    --ink-soft: #4a4a4a;
    --orange: #f2a024;
    --band: #e4e4e4;
    --photo-light: #f3f3f3;
    --photo-mid: #b9b9b9;
    --photo-dark: #6e6e6e;
  }
  * { margin: 0; padding: 0; box-sizing: border-box; }
  html, body { width: 900px; height: 1200px; overflow: hidden; background: var(--paper); }
  .flyer {
    position: relative;
    width: 900px; height: 1200px;
    background: var(--paper);
    font-family: "Open Sans", Arial, sans-serif;
    color: var(--ink);
    text-align: center;
  }
  .hero-photo {
    position: absolute; left: 0; top: 0;
    width: 900px; height: 700px;
    background:
      radial-gradient(ellipse 38% 42% at 40% 40%, var(--photo-light) 0%, rgba(243,243,243,0) 70%),
      radial-gradient(ellipse 34% 40% at 68% 42%, var(--photo-dark) 0%, rgba(110,110,110,0) 75%),
      radial-gradient(ellipse 30% 30% at 12% 12%, #ffffff 0%, rgba(255,255,255,0) 70%),
      radial-gradient(ellipse 30% 30% at 90% 10%, #ffffff 0%, rgba(255,255,255,0) 70%),
      linear-gradient(180deg, var(--photo-mid) 0%, #cfcfcf 70%, var(--paper) 100%);
  }
  .hero-strip {
    position: absolute; left: 0; top: 600px;
    width: 900px; height: 80px;
    background: rgba(255,255,255,0.55);
  }
  .brand {
    position: absolute; left: 0; top: 740px; width: 100%;
    font-family: "Open Sans", Arial, sans-serif;
    font-weight: 600; font-size: 34px; line-height: 44px;
    color: var(--ink);
  }
  .event-call {
    position: absolute; left: 0; top: 836px; width: 100%;
    color: var(--orange);
    font-family: "Montserrat", Arial, sans-serif;
    font-weight: 500; font-size: 19px; line-height: 25px;
  }
  .headline {
    position: absolute; left: 0; top: 900px; width: 100%;
    font-family: "Montserrat", Arial, sans-serif;
    font-weight: 600; font-size: 30px; color: var(--ink);
  }
  .pitch {
    position: absolute; left: 0; top: 946px; width: 100%;
    font-size: 21px; line-height: 30px; color: var(--ink-soft);
  }
  .book-button {
    position: absolute; left: 335px; top: 1080px;
    width: 230px; height: 34px;
    background: var(--orange); color: var(--paper);
    font-family: "Montserrat", Arial, sans-serif;
    font-size: 17px; font-weight: 500; line-height: 34px;
  }
  .contact {
    position: absolute; left: 0; top: 1124px; width: 100%;
    font-size: 17px; color: var(--ink-soft);
  }
  .contact .phone { margin-left: 14px; }
  .web-band {
    position: absolute; left: 0; top: 1154px;
    width: 900px; height: 34px;
    background: var(--band);
    font-family: "Montserrat", Arial, sans-serif;
    font-size: 19px; font-weight: 600; letter-spacing: 9px;
    line-height: 34px; color: var(--ink);
  }
</style>
</head>
<body>
  <main class="flyer">
    <div class="hero-photo" role="img" aria-label="Soft black and white photograph of a young couple embracing, framed by white blossoms"></div>
    <div class="hero-strip"></div>

    <header class="brand">Kindred Path Guides</header>

    <p class="event-call">Calling all Singles Soulmate Workshop<br>Finding your Ideal Partner</p>

    <h1 class="headline">How to Find your Perfect Match</h1>

    <p class="pitch">
      Are you sick of being used as an emotional punching bag?<br>
      Are you ready to find your Mr/Mrs Right?<br>
      Let me share with you the steps I used to find My Mrs Right.<br>
      The pathway to Relationship Happiness
    </p>

    <div class="book-button">Limited spaces Book Now</div>

    <p class="contact"><span class="name">Dom Harlow</span><span class="phone">0400 555 218</span></p>

    <footer class="web-band">www.kindredpathguides.com</footer>
  </main>
</body>
</html>
```